K Forgeworks Design and Analytics
Tech Consulting Company
K Forgeworks Design and Analytics - Information Technology
Creative Brief
Simple
Marcus Pellham
President/CEO
748 South Quillon Ave Baltimore, MD 21287
m.pellham@kfda-mail.com
Just the Logo on the back

```html
<!DOCTYPE html>
<html lang="en">
<head>
<meta charset="utf-8">
<title>K Forgeworks Design and Analytics – Business Cards</title>
<link rel="stylesheet" href="https://fonts.googleapis.com/css2?family=Montserrat:wght@400;600;700&display=swap">
<style>
  :root {
    --stage: #d9d9d9;
    --paper-light: #ffffff;
    --paper-dark: #1c1c1c;
    --ink-dark: #1a1a1a;
    --ink-light: #f2f2f2;
    --ink-muted: #8a8a8a;
    --band: #111111;
    --band-alt: #e9e9e9;
  }
  * { box-sizing: border-box; margin: 0; padding: 0; }
  html, body {
    width: 1200px; height: 451px; overflow: hidden;
    background: var(--stage);
    font-family: "Montserrat", sans-serif;
  }
  .stage { position: relative; width: 1200px; height: 451px; }
  .card {
    position: absolute; top: 125px;
    width: 262px; height: 150px;
    overflow: hidden;
    box-shadow: 0 3px 8px rgba(0,0,0,.18);
  }
  .card--light { background: var(--paper-light); color: var(--ink-dark); }
  .card--dark  { background: var(--paper-dark);  color: var(--ink-light); }
  .card--a { left: 34px; }
  .card--b { left: 308px; }
  .card--c { left: 628px; }
  .card--d { left: 902px; }

  .brand {
    display: flex; align-items: center; gap: 6px;
    font-weight: 700; letter-spacing: .03em; text-transform: uppercase;
    white-space: nowrap;
  }
  .brand__mark { width: 7px; height: 7px; border-radius: 50%; background: currentColor; flex: none; }

  .front .brand { position: absolute; left: 14px; top: 20px; font-size: 12px; }
  .front .tagline {
    position: absolute; left: 14px; top: 38px;
    font-size: 4.5px; letter-spacing: .06em; text-transform: uppercase;
    color: var(--ink-muted); white-space: nowrap;
  }
  .front .nameband {
    position: absolute; left: 0; top: 56px; width: 132px; height: 22px;
    padding: 3px 0 0 14px;
  }
  .card--light .nameband { background: var(--band); color: var(--ink-light); }
  .card--dark  .nameband { background: var(--band-alt); color: var(--ink-dark); }
  .nameband__name { font-size: 8px; font-weight: 600; letter-spacing: .06em; text-transform: uppercase; display: block; white-space: nowrap; }
  .nameband__title { font-size: 5px; letter-spacing: .1em; text-transform: uppercase; display: block; }
  .front .contact {
    position: absolute; left: 14px; top: 92px;
    font-size: 5px; line-height: 1.6; list-style: none; white-space: nowrap;
  }
  .front .slashes { position: absolute; right: 0; bottom: 0; }

  .back .brand {
    position: absolute; left: 0; right: 0; top: 56px;
    justify-content: center; font-size: 20px;
  }
  .back .website {
    position: absolute; left: 0; right: 0; top: 110px;
    text-align: center; font-size: 7px; letter-spacing: .08em;
  }
</style>
</head>
<body>
<main class="stage">

  <article class="card card--light front card--a">
    <div class="brand"><span class="brand__mark"></span>K Forgeworks</div>
    <p class="tagline">K Forgeworks Design and Analytics</p>
    <div class="nameband">
      <span class="nameband__name">Marcus Pellham</span>
      <span class="nameband__title">President/CEO</span>
    </div>
    <ul class="contact">
      <li>748 South Quillon Ave Baltimore, MD 21287</li>
      <li>410.555.0147</li>
      <li>m.pellham@kfda-mail.com</li>
    </ul>
    <svg class="slashes" width="110" height="150" viewBox="0 0 110 150" aria-hidden="true">
      <line x1="40" y1="0" x2="10" y2="150" stroke="#1a1a1a" stroke-width="1"/>
      <line x1="110" y1="40" x2="70" y2="150" stroke="#1a1a1a" stroke-width="1"/>
    </svg>
  </article>

  <article class="card card--light back card--b">
    <div class="brand"><span class="brand__mark"></span>K Forgeworks</div>
    <p class="website">www.kfda-mail.com</p>
  </article>

  <article class="card card--dark front card--c">
    <div class="brand"><span class="brand__mark"></span>K Forgeworks</div>
    <p class="tagline">K Forgeworks Design and Analytics</p>
    <div class="nameband">
      <span class="nameband__name">Marcus Pellham</span>
      <span class="nameband__title">President/CEO</span>
    </div>
    <ul class="contact">
      <li>748 South Quillon Ave Baltimore, MD 21287</li>
      <li>410.555.0147</li>
      <li>m.pellham@kfda-mail.com</li>
    </ul>
    <svg class="slashes" width="110" height="150" viewBox="0 0 110 150" aria-hidden="true">
      <line x1="40" y1="0" x2="10" y2="150" stroke="#f2f2f2" stroke-width="1"/>
      <line x1="110" y1="40" x2="70" y2="150" stroke="#f2f2f2" stroke-width="1"/>
    </svg>
  </article>

  <article class="card card--dark back card--d">
    <div class="brand"><span class="brand__mark"></span>K Forgeworks</div>
    <p class="website">www.kfda-mail.com</p>
  </article>

</main>
</body>
</html>
```